Consulting im Pharmaproduktionsbereich sucht Webdesign
Zielgruppe
Consulting im Pharmaproduktionsbereich.
Bitte lesen Sie dazu die PowerPoint.
Aufgabenstellung
Im Anhang finden Sie eine Powerpoint Datei, von welcher die 'Home' und 'Referenz'seite Teil dieser Auschreibung sind.

```html
<!DOCTYPE html>
<html lang="de">
<head>
<meta charset="utf-8">
<title>Kestrel Tec GmbH – Home</title>
<link href="https://fonts.googleapis.com/css2?family=Tinos:wght@700&family=Open+Sans:ital,wght@0,400;1,400&family=Raleway:wght@400;600&family=Source+Sans+3:wght@400&display=swap" rel="stylesheet">
<style>
:root{
  --blue:#1b4a8a;
  --blue-bar:#164a8a;
  --slate:#5f7681;
  --hero-box:rgba(122,137,146,.93);
  --band:#f0f0f2;
  --field:#f1f1f3;
  --ink:#1d1d1d;
  --muted:#5c6d78;
  --white:#ffffff;
}
*{margin:0;padding:0;box-sizing:border-box}
html,body{width:717px;height:1200px;overflow:hidden;background:var(--white)}
body{position:relative;font-family:"Open Sans",sans-serif;color:var(--ink)}
.abs{position:absolute}
.hero-photo{left:0;top:0;width:717px;height:390px;background:linear-gradient(160deg,#b9c9d8 0%,#d6e0e9 35%,#f2f2f0 60%,#e9d9c8 80%,#c9b49c 100%)}
.logo{display:flex;align-items:center;gap:6px;font-family:"Open Sans",sans-serif;font-weight:400;color:var(--blue)}
.logo-mark{background:var(--blue)}
.nav{right:37px;top:15px;font-family:"Raleway",sans-serif;font-size:9.5px;color:#1e2b3a;letter-spacing:.2px}
.nav span{margin:0 5px}
.nav .active{font-weight:600;color:#000}
.hero-box{left:0;top:102px;width:290px;height:137px;background:var(--hero-box)}
.hero-title{left:32px;top:116px;font-family:"Tinos",serif;font-weight:700;font-size:25px;line-height:39px;color:var(--white)}
.hero-btn{left:32px;top:202px;width:145px;height:23px;border:1px solid var(--white);color:var(--white);font-family:"Source Sans 3",sans-serif;font-size:10px;letter-spacing:.4px;display:flex;align-items:center;justify-content:center}
.intro-panel{left:82px;top:358px;width:561px;height:40px;background:var(--white)}
.intro-title{left:0;width:717px;top:377px;text-align:center;font-family:"Tinos",serif;font-weight:700;font-size:24px;color:var(--blue)}
.intro-sub{left:0;width:717px;top:404px;text-align:center;font-style:italic;font-size:13px;color:var(--muted)}
.intro-text{left:140px;width:455px;top:428px;text-align:center;font-style:italic;font-size:8.4px;line-height:10.5px}
.card{top:471px;height:149px}
.card-label{background:var(--slate);color:var(--white);font-family:"Tinos",serif;font-weight:700;font-size:24px;display:flex;align-items:center;justify-content:center}
.value-card{background:var(--slate);color:var(--white);text-align:center}
.value-card h3{font-family:"Tinos",serif;font-weight:700;font-size:23px;margin-top:11px;line-height:24px}
.value-card p{font-style:italic;font-size:9.6px;line-height:13px;padding:0 18px}
.band{left:0;top:727px;width:717px;height:213px;background:var(--band)}
.person{left:31px;top:650px;width:295px;height:290px;border-radius:140px 140px 0 0;background:linear-gradient(180deg,#d9c7bb 0%,#ece8e6 45%,#f7f7f8 100%)}
.cta-title{left:356px;top:759px;font-family:"Tinos",serif;font-weight:700;font-size:27px;line-height:34px;color:var(--blue)}
.cta-sub{left:356px;top:862px;font-family:"Source Sans 3",sans-serif;font-size:22px;color:var(--muted)}
.pen-photo{left:33px;top:977px;width:156px;height:156px;border-radius:50%;background:radial-gradient(circle at 55% 50%,#e7d3c5 0%,#dfe4ea 55%,#c9d3dd 100%)}
.address{left:230px;font-family:"Source Sans 3",sans-serif;font-size:8px;line-height:10px;color:#1a1a1a;display:flex;gap:5px;align-items:flex-start}
.address svg{flex:none}
.kontakt-title{left:453px;top:968px;font-family:"Tinos",serif;font-weight:700;font-size:24px;color:var(--blue)}
.label{left:454px;font-family:"Source Sans 3",sans-serif;font-size:6.6px;color:#222;display:flex;align-items:center;gap:3px}
.field{left:453px;width:230px;height:20px;background:var(--field)}
.select{display:flex;align-items:center;justify-content:space-between;padding:0 6px 0 4px;font-style:italic;font-size:6.4px}
.note{left:455px;top:1118px;font-size:4.4px;line-height:7.5px;color:#444}
.send{left:623px;top:1118px;width:61px;height:17px;background:var(--slate);color:var(--white);font-family:"Source Sans 3",sans-serif;font-size:8px;display:flex;align-items:center;justify-content:center;letter-spacing:.3px}
.footer{left:0;top:1167px;width:717px;height:33px;background:var(--blue-bar);color:#dce6f3;font-family:"Raleway",sans-serif;font-size:8.4px;display:flex;align-items:center;justify-content:space-between;padding:0 33px}
.footer nav span{margin:0 5px}
.footer .active{font-weight:600;color:var(--white);margin-left:0}
</style>
</head>
<body>
<div class="abs hero-photo" role="img" aria-label="Weißes modernes Gebäude mit Holzfenstern vor blauem Himmel"></div>

<div class="abs logo" style="left:36px;top:22px;font-size:21px">
  <span class="logo-mark" style="width:20px;height:20px"></span>Kestrel Tec
</div>

<nav class="abs nav">
  <span class="active">HOME</span>|<span>REFERENZEN</span>|<span>KONTAKT</span>|<span>IMPRESSUM</span>
</nav>

<div class="abs hero-box"></div>
<h1 class="abs hero-title">IHR GESCHÄFT IST<br>UNSER GESCHÄFT</h1>
<div class="abs hero-btn">JETZT KONTAKT AUFNEHMEN</div>

<div class="abs intro-panel"></div>
<h2 class="abs intro-title">Als spezialisierter Anbieter</h2>
<p class="abs intro-sub">schaffen wir Wert in der Pharma-Produktion</p>
<p class="abs intro-text">Mit langjähriger Erfahrung in Abläufen und überlegener Technologie setzt ein Netzwerk von Spitzenleuten schnell und pragmatisch um Sicht- und messbar in Ihrer Bilanz</p>

<div class="abs card" style="left:36px;width:206px;background:linear-gradient(135deg,#3e444c 0%,#c9c4bf 45%,#eeeeee 100%)" role="img" aria-label="Geschäftsmann und Ärztin im Gespräch am Schreibtisch"></div>
<div class="abs card-label" style="left:76px;top:586px;width:121px;height:32px">Abläufe</div>

<div class="abs card" style="left:256px;width:205px;background:linear-gradient(160deg,#dfe8f0 0%,#9fb3c6 50%,#cfd8e0 100%)" role="img" aria-label="Labor mit Monitoren und Mitarbeiter in Schutzkleidung"></div>
<div class="abs card-label" style="left:278px;top:582px;width:159px;height:32px">Technologie</div>

<div class="abs card value-card" style="left:479px;width:206px">
  <h3>Wert</h3>
  <p>Ob Sie Topline mehr Kapazität generi-eren wollen, oder Bottomline einzelne Kostenpositionen reduzieren: Wir achten auf das für Ihren Betrieb pas-sende Werteversprechen und liefern schnell ergebniswirksam. Unnötiger Firlefanz bleibt weg.</p>
</div>

<div class="abs band"></div>
<div class="abs person" role="img" aria-label="Lächelnde Ärztin im weißen Kittel mit Stethoskop zeigt Daumen hoch"></div>
<h2 class="abs cta-title">Wollen auch Sie bei der<br>Optimierung Ihrer Kosten<br>einen Schritt weitergehen?</h2>
<p class="abs cta-sub">Kontaktieren Sie uns.</p>

<div class="abs pen-photo" role="img" aria-label="Hand mit Füllfederhalter beim Unterschreiben"></div>

<div class="abs logo" style="left:232px;top:982px;font-size:22px">
  <span class="logo-mark" style="width:22px;height:22px"></span>Kestrel Tec
</div>

<div class="abs address" style="top:1027px">
  <svg width="9" height="11" viewBox="0 0 9 11"><path d="M4.5 0.5A3.6 3.6 0 0 0 0.9 4.1c0 2.6 3.6 6.4 3.6 6.4s3.6-3.8 3.6-6.4A3.6 3.6 0 0 0 4.5 0.5z" fill="none" stroke="#1b4a8a" stroke-width="1.2"/><circle cx="4.5" cy="4.1" r="1.2" fill="#1b4a8a"/></svg>
  <div>Kestrel Tec<br>Lindenweg 12, 70000 Musterstadt</div>
</div>
<div class="abs address" style="top:1057px">
  <svg width="9" height="11" viewBox="0 0 9 11"><rect x="1.5" y="0.6" width="6" height="9.8" rx="1" fill="none" stroke="#1b4a8a" stroke-width="1.1"/><line x1="3.5" y1="8.6" x2="5.5" y2="8.6" stroke="#1b4a8a"/></svg>
  <div>Tel. (0) 5566 / 120 300</div>
</div>
<div class="abs address" style="top:1075px">
  <svg width="9" height="9" viewBox="0 0 9 9"><circle cx="4.5" cy="4.5" r="3.8" fill="none" stroke="#1b4a8a" stroke-width="1.1"/><path d="M0.7 4.5h7.6M4.5 0.7c-2 2.4-2 5.2 0 7.6M4.5 0.7c2 2.4 2 5.2 0 7.6" fill="none" stroke="#1b4a8a" stroke-width=".7"/></svg>
  <div>info@kestrel-tec.de</div>
</div>

<h2 class="abs kontakt-title">KONTAKT</h2>
<div class="abs label" style="top:1001px">
  <svg width="6" height="6" viewBox="0 0 6 6"><circle cx="3" cy="1.6" r="1.4" fill="#222"/><path d="M0.3 6c0-2 1.2-3 2.7-3s2.7 1 2.7 3z" fill="#222"/></svg>Ihr Name*
</div>
<div class="abs field" style="top:1014px"></div>
<div class="abs label" style="top:1040px">
  <svg width="7" height="6" viewBox="0 0 7 6"><path d="M0.3 1.8C1.5 0.4 5.5 0.4 6.7 1.8L6 2.6 4.8 2.2V1.5H2.2v.7L1 2.6z" fill="#222"/><rect x="1.3" y="3" width="4.4" height="3" fill="#222"/></svg>Telefonnummer*
</div>
<div class="abs field" style="top:1051px"></div>
<div class="abs label" style="top:1078px">
  <svg width="6" height="6" viewBox="0 0 6 6"><circle cx="3" cy="1.6" r="1.4" fill="#222"/><path d="M0.3 6c0-2 1.2-3 2.7-3s2.7 1 2.7 3z" fill="#222"/></svg>Ich habe Interesse an
</div>
<div class="abs field select" style="top:1089px">
  <span>einem kostenfreien Erstgespräch</span>
  <svg width="10" height="7" viewBox="0 0 10 7"><path d="M1 1.2l4 4 4-4" fill="none" stroke="#111" stroke-width="1.8"/></svg>
</div>
<p class="abs note">Die mit * gekennzeichneten Felder sind Pflichtfelder.<br>Ihre Daten werden vertraulich behandelt.</p>
<div class="abs send">AB DIE POST</div>

<footer class="abs footer">
  <nav><span class="active">HOME</span>|<span>REFERENZEN</span> |<span>KONTAKT</span> |<span>IMPRESSUM</span> |<span>DATENSCHUTZ</span></nav>
  <div>© Kestrel Tec GmbH 2019. All rights reserved.</div>
</footer>
</body>
</html>
```